Business Card Design

Business card design.

Business card is to have logo, website address and email address.

Website is www.brightkettle.ie
Email is info@brightkettle.ie
Logo uploaded

I have ordered Business Card Printing via Print Harbor, the Double-sided colour printed option with gloss finish.

Industry/Entity Type

Business

```html
<!DOCTYPE html>
<html lang="en">
<head>
<meta charset="utf-8">
<title>Bright Kettle – Business Card</title>
<link rel="stylesheet" href="https://fonts.googleapis.com/css2?family=Crimson+Text:ital@1&family=Cabin:wght@700&display=swap">
<style>
  :root {
    --card-black: #000000;
    --brand-red: #e8141b;
    --mug-white: #f2f2f2;
    --mug-grey: #bdbdbd;
    --mug-red: #d50000;
    --ink: #140000;
  }
  html, body {
    margin: 0;
    padding: 0;
    overflow: hidden;
    background: var(--card-black);
  }
  .card {
    position: relative;
    width: 1200px;
    height: 686px;
    background: var(--card-black);
    overflow: hidden;
  }
  .mug-row {
    position: absolute;
    left: 52px;
    top: 135px;
    width: 1096px;
    height: 293px;
    border-radius: 146px;
    background: linear-gradient(90deg,
      var(--mug-grey) 0%,
      var(--mug-white) 15%,
      var(--mug-white) 33%,
      var(--mug-red) 42%,
      var(--mug-red) 58%,
      var(--mug-white) 67%,
      var(--mug-white) 85%,
      var(--mug-grey) 100%);
  }
  .contact {
    position: absolute;
    left: 801px;
    height: 49px;
    display: flex;
    gap: 10px;
  }
  .contact--email { top: 450px; }
  .contact--web { top: 512px; }
  .contact__marker {
    width: 37px;
    height: 100%;
    background: var(--brand-red);
  }
  .contact__text {
    width: 348px;
    height: 100%;
    background: var(--brand-red);
    color: var(--ink);
    font-family: "Crimson Text", Georgia, serif;
    font-style: italic;
    font-size: 33px;
    line-height: 49px;
    padding-left: 8px;
    box-sizing: border-box;
    white-space: nowrap;
  }
  .region-band {
    position: absolute;
    left: 0;
    top: 578px;
    width: 1200px;
    height: 108px;
  }
  .region-band__label {
    position: absolute;
    right: 10px;
    top: 598px;
    font-family: "Cabin", Arial, sans-serif;
    font-weight: 700;
    font-size: 32px;
    line-height: 40px;
    letter-spacing: -0.5px;
    color: var(--ink);
  }
</style>
</head>
<body>
<main class="card">
  <div class="mug-row" role="img" aria-label="Row of smiling white mug faces with one frowning red face in the centre"></div>

  <div class="contact contact--email">
    <span class="contact__marker"></span>
    <span class="contact__text">info@brightkettle.ie</span>
  </div>
  <div class="contact contact--web">
    <span class="contact__marker"></span>
    <span class="contact__text">www.brightkettle.ie</span>
  </div>

  <svg class="region-band" width="1200" height="108" viewBox="0 0 1200 108" aria-hidden="true">
    <rect x="0" y="0" width="1200" height="108" fill="var(--brand-red)"/>
    <rect x="580" y="0" width="6" height="108" fill="var(--card-black)"/>
    <rect x="596" y="0" width="6" height="108" fill="var(--card-black)"/>
    <rect x="622" y="0" width="6" height="108" fill="var(--card-black)"/>
  </svg>
  <div class="region-band__label">Ireland, United Kingdom</div>
</main>
</body>
</html>
```